Very visible CoWorking Building Sign overlooking downtown LA and 110 freeway

Our building is drab but very visible and in the best location. We need a great sign for our monolith that overlooks downtown LA and the 100 freeway. We are a new CoWorking business and would like to have a few things we do on the sign: private offices, virtual offices, CoWorking Lounge. Everything we have seen is ho-hum. Can you get us noticed? We need people to know what we do and that we are here but in a creative, professional, unique sign.
Target Market(s)
People who have a business in DTLA, remote workers and those who work from home who need a professional address.
Requirements
Must have
- Our logo (which can be somewhat reimagined) which has our address 2740 on it. The three things we focus on: Private Offices, Virtual Offices, CoWorking Lounge. Incorporate some Navy. Readable from several hundred feet away.
Nice to have
- Mural feel? Something inspirational in this crazy COVID times? Graphics? Color block. I like the idea of decorative but it has to be readable as a building sign. The same with the use of colors. Our colors are grays and navy but with a pop of the chartreuse (we have 2 velvet chartreuse chairs in the space). Helpful to view our website: Halvorn2740.com.
Should not have
- Not too graffiti. Keep it professional but unique and wow.

```html
<!DOCTYPE html>
<html lang="en">
<head>
<meta charset="utf-8">
<title>2740 Halvorn – Building Sign</title>
<link rel="stylesheet" href="https://fonts.googleapis.com/css2?family=Libre+Baskerville:wght@700&display=swap">
<style>
  :root {
    --navy: #13294b;
    --navy-soft: #3d5074;
    --navy-light: #7d8aa3;
    --chartreuse: #8dc63f;
    --chartreuse-deep: #82bb36;
    --paper: #ffffff;
    --backdrop: #e4e5e7;
  }
  html, body {
    margin: 0;
    padding: 0;
    width: 1200px;
    height: 1097px;
    overflow: hidden;
    background: var(--backdrop);
  }
  .sign {
    position: absolute;
    left: 283px;
    top: 22px;
    width: 703px;
    height: 1170px;
    background: var(--paper);
    transform: scale(0.9);
    transform-origin: top left;
    box-shadow: 0 2px 10px rgba(0,0,0,0.08);
    font-family: "Libre Baskerville", "Times New Roman", serif;
  }
  .sign-frame {
    position: absolute;
    inset: 0;
  }
  .ornament {
    position: absolute;
    left: 150px;
    width: 400px;
    height: 56px;
    border-radius: 28px;
    background: linear-gradient(90deg, var(--navy-light) 0%, var(--navy-soft) 30%, var(--navy) 50%, var(--navy-soft) 70%, var(--navy-light) 100%);
  }
  .ornament--top { top: 32px; }
  .ornament--bottom { top: 1078px; }
  .brand {
    position: absolute;
    left: 0;
    right: 0;
    top: 150px;
    text-align: center;
    color: var(--navy);
    font-weight: 700;
    line-height: 1;
  }
  .brand-number {
    display: block;
    font-size: 56px;
    letter-spacing: 8px;
  }
  .brand-name {
    display: block;
    margin-top: 18px;
    font-size: 84px;
    letter-spacing: 2px;
  }
  .accent-bar {
    position: absolute;
    left: 287px;
    top: 357px;
    width: 128px;
    height: 8px;
    background: var(--chartreuse);
  }
  .service {
    position: absolute;
    left: 84px;
    width: 600px;
    height: 186px;
  }
  .service-icon {
    position: absolute;
    left: 0;
    top: 0;
    width: 186px;
    height: 186px;
    border-radius: 50%;
    background: radial-gradient(circle at 50% 45%, var(--chartreuse) 0%, var(--chartreuse) 55%, var(--chartreuse-deep) 100%);
  }
  .service-name {
    position: absolute;
    left: 220px;
    top: 46px;
    margin: 0;
    color: var(--navy);
    font-size: 42px;
    font-weight: 700;
    line-height: 50px;
    letter-spacing: 0.5px;
  }
  .service--private { top: 377px; }
  .service--virtual { top: 600px; }
  .service--lounge { top: 824px; }
  .divider {
    position: absolute;
    left: 322px;
    width: 203px;
    height: 2px;
    background: var(--chartreuse);
  }
  .divider--one { top: 580px; }
  .divider--two { top: 806px; }
</style>
</head>
<body>
  <div class="sign">
    <svg class="sign-frame" width="703" height="1170" viewBox="0 0 703 1170" fill="none" stroke="var(--navy)">
      <!-- outer frame, open at the centre top and bottom -->
      <path d="M140 42 H35 V1132 H140 M560 1132 H670 V42 H560" stroke-width="2"/>
      <!-- inner frame -->
      <path d="M140 53 H46 V1121 H140 M560 1121 H659 V53 H560" stroke-width="1"/>
      <g fill="var(--navy)" stroke="none">
        <polygon points="46,53 66,53 46,73"/>
        <polygon points="659,53 639,53 659,73"/>
        <polygon points="46,1121 66,1121 46,1101"/>
        <polygon points="659,1121 639,1121 659,1101"/>
      </g>
    </svg>

    <div class="ornament ornament--top" role="img" aria-label="Decorative navy scrollwork flourish"></div>

    <div class="brand">
      <span class="brand-number">2740</span>
      <span class="brand-name">HALVORN</span>
    </div>
    <div class="accent-bar"></div>

    <div class="service service--private">
      <div class="service-icon" role="img" aria-label="White line icon of a private office desk, chair, lamp and wall art"></div>
      <h2 class="service-name">PRIVATE<br>OFFICES</h2>
    </div>
    <div class="divider divider--one"></div>

    <div class="service service--virtual">
      <div class="service-icon" role="img" aria-label="White line icon of a reception desk with mail envelope and plant"></div>
      <h2 class="service-name">VIRTUAL<br>OFFICES</h2>
    </div>
    <div class="divider divider--two"></div>

    <div class="service service--lounge">
      <div class="service-icon" role="img" aria-label="White line icon of two coworkers chatting at a shared table"></div>
      <h2 class="service-name">COWORKING<br>LOUNGE</h2>
    </div>

    <div class="ornament ornament--bottom" role="img" aria-label="Decorative navy scrollwork flourish"></div>
  </div>
</body>
</html>
```